Buch-/eBook-Cover zum Thema Magersucht
Zielgruppe
Ich bin Autorin und suche ein passendes Buchcover. Die Zielgruppe für dieses Buch sind Eltern von magersüchtigen Kindern sowie interessierte medizinische und therapeutische Fachkräfte.
Aufgabenstellung
Bei meinem Buch handelt es sich um einen Ratgeber zur Behandlung von Magersucht bei Kindern und Jugendlichen.
Folgendes muss auf die Vorderseite des Buches:
Titel: Brot baut Brücken
Untertitel: Gemeinsamer Alltag nach der Klinikzeit
Helke Brunsmann
Ich wünsche mir ein einfühlsames Cover, das die Schwere der Krankheit spiegelt, aber auch die Hoffnung auf Heilung. Bitte keine plumpen Bilder von Waage, Massband oder dünnen Körpern.
Der Klappentext im Word-Dokument ist für die Rückseite des Buchcovers.

```html
<!DOCTYPE html>
<html lang="de">
<head>
<meta charset="utf-8">
<title>Brot baut Brücken – Buchcover</title>
<link rel="stylesheet" href="https://fonts.googleapis.com/css2?family=Lato:wght@400&family=Ubuntu:wght@500;700&display=swap">
<style>
  :root {
    --page-bg: #eeeeee;
    --cover-pink: #f8cfdd;
    --cover-pink-light: #fbe3ec;
    --cover-pink-deep: #f1b6cc;
    --title-purple: #6a2f8c;
    --accent-teal: #2b8272;
    --glow-white: #ffffff;
    --figure-violet: #a35aa8;
  }
  * { margin: 0; padding: 0; box-sizing: border-box; }
  html, body {
    width: 1200px;
    height: 1193px;
    overflow: hidden;
    background: var(--page-bg);
  }
  .book-cover {
    position: absolute;
    left: 238px;
    top: 53px;
    width: 724px;
    height: 1088px;
    overflow: hidden;
    background:
      radial-gradient(ellipse 60% 40% at 20% 95%, var(--cover-pink-deep), transparent 70%),
      radial-gradient(ellipse 50% 35% at 85% 90%, var(--cover-pink-deep), transparent 70%),
      linear-gradient(180deg, var(--cover-pink-light) 0%, var(--cover-pink) 55%, var(--cover-pink-light) 100%);
    text-align: center;
  }
  .author {
    position: absolute;
    top: 40px;
    left: 0;
    right: 0;
    font-family: "Lato", sans-serif;
    font-weight: 400;
    font-size: 34px;
    letter-spacing: 0.5px;
    color: var(--accent-teal);
    text-transform: uppercase;
  }
  .title {
    position: absolute;
    top: 128px;
    left: 0;
    right: 0;
    font-family: "Ubuntu", sans-serif;
    color: var(--title-purple);
    line-height: 1;
  }
  .title-line { display: block; }
  .title-line--strong {
    font-weight: 700;
    font-size: 96px;
    letter-spacing: -1px;
  }
  .title-line--soft {
    font-weight: 500;
    font-size: 76px;
    margin: 22px 0 20px;
  }
  .cover-illustration {
    position: absolute;
    left: 60px;
    top: 480px;
    width: 604px;
    height: 450px;
    background:
      radial-gradient(ellipse 10% 42% at 50% 50%, var(--figure-violet), transparent 90%),
      radial-gradient(ellipse 28% 50% at 50% 40%, var(--glow-white), transparent 80%),
      radial-gradient(ellipse 50% 50% at 50% 50%, var(--cover-pink-light), transparent 100%);
    opacity: 0.9;
  }
  .subtitle {
    position: absolute;
    top: 940px;
    left: 0;
    right: 0;
    font-family: "Ubuntu", sans-serif;
    font-weight: 500;
    font-size: 38px;
    line-height: 1.5;
    color: var(--accent-teal);
  }
</style>
</head>
<body>
  <main class="book-cover">
    <p class="author">Helke Brunsmann</p>
    <h1 class="title">
      <span class="title-line title-line--strong">BROT</span>
      <span class="title-line title-line--soft">baut</span>
      <span class="title-line title-line--strong">BRÜCKEN</span>
    </h1>
    <div class="cover-illustration" role="img" aria-label="Aquarell-Illustration: Silhouette eines Mädchens, das im Gegenlicht aus rosa Nebel auf den Betrachter zugeht"></div>
    <p class="subtitle">Gemeinsamer Alltag<br>nach der Klinikzeit</p>
  </main>
</body>
</html>
```